Renny Osbert Personalised Health, Performance and Longevity Exec Coach

Business Card for www.rennyosbert.example site. It is a trust site and I use it for 1:1 relatable connections. It is the one I use for building intimate 1:1 trust building and Exec Coaching Services and programs for high wealth individuals and corporates. I also have a commercial programmatic site of my personal health products and services and programs for main stream one to many. www.halfwaypioneer.example that can also provoke thought for the www.rennyosbert.example business card. (mind you will get a separate business card for that site, but want to provide context). It has a logo which you may want to draw from in designing the rennyosbert business card which is personal and is about building my brand. There is also a rennyosbert personal Chirply page and rennyosbert business Chirply page. I am a Certified Talent Compass 3.1 Coach with Verrow and you can get a corporate brief of me on there to give you more context https://www.verrowtalenthub.example/coach/en-us/directory?search=renny

Target Market(s)

Being a Personalised Health Coach I am focused on Health>Performance>Longevity>Wellbeing. Target market is Executives /High Wealth individuals/Corporates. I am most relatable to the IT industry as I was ion it building partnerships for IT companies for 28+ years.

Industry/Entity Type

Health And Wellness

Contact Information for Business Card

Name: Renny Osbert
email: renny@rennyosbert.example
Phone: Australia +61 491352864 Singapore +65 83426109

Font styles to use
Sans Serif
Other font styles liked:
• Arial and Calibra could work?

Colors

Designer to choose colors to be used in the design.

Requirements
Must have
• It must be a no BS design that is intimate. In keeping with the rennyosbert.example website I'm guessing grey scale. It may be printed on plastic as well for durability and a point of difference. It must have people feeling trust and feeling safe to be 1:1 personal. It's about helping people move from stuck to sustainable change. Moving them to a healthier state, increasing performance if and where they want, longevity and well being.
Nice to have
• On the back you can place a logo that is in line with what I have as a colourful mandala at www.halfwaypioneer.example. It will be on the landing page and top left of each page in that site. A greyscale simpler version to create linkage to my philosophy. Also you could have the continuum of Personalised Health > > Performance > Longevity > Wellbeing as well or instead of in your designs some how infographcially represented if not using the existing logo at Halfwaypioneer.example
Should not have
• Clutter is a no no. Keep it clean, easy to read, no BS feel. Must be authentic and warm yet smart.

```html
<!DOCTYPE html>
<html lang="en">
<head>
<meta charset="utf-8">
<title>Renny Osbert – Business Card</title>
<link href="https://fonts.googleapis.com/css2?family=Montserrat:wght@500;600&family=Nothing+You+Could+Do&display=swap" rel="stylesheet">
<style>
  :root{
    --stage:#000000;
    --card:#ffffff;
    --brand-blue:#00a3e0;
    --band-grey:#ececec;
    --band-grey-light:#f4f4f4;
    --ink:#111111;
    --text-grey:#58595b;
    --dot-cyan:#00a8e8;
    --dot-navy:#2e3192;
    --dot-magenta:#ec008c;
    --dot-orange:#f7941d;
    --dot-green:#8dc63f;
  }
  *{box-sizing:border-box;margin:0;padding:0}
  html,body{width:1155px;height:1200px;overflow:hidden;background:var(--stage)}
  .stage{position:relative;width:1155px;height:1200px}
  .card{position:absolute;left:203px;width:749px;height:428px;background:var(--card);overflow:hidden}
  .card--front{top:141px}
  .card--back{top:632px}

  .front-art{position:absolute;left:0;top:0;width:749px;height:428px}

  .name{
    position:absolute;left:390px;top:98px;
    font-family:"Nothing You Could Do",cursive;
    font-size:42px;color:var(--ink);letter-spacing:1px;white-space:nowrap;
  }
  .contact-list{position:absolute;left:390px;top:190px;list-style:none}
  .contact-item{
    position:relative;height:37px;padding-left:31px;
    display:flex;align-items:center;
    font-family:"Montserrat",sans-serif;font-weight:600;font-size:17px;
    color:var(--text-grey);white-space:nowrap;
  }
  .contact-icon{position:absolute;left:0;top:50%;transform:translateY(-50%);width:19px;height:19px;fill:var(--text-grey)}

  .brand-mark{
    position:absolute;left:0;right:0;top:130px;
    display:flex;justify-content:center;align-items:center;gap:12px;
    font-family:"Montserrat",sans-serif;font-weight:600;font-size:26px;
    color:var(--text-grey);letter-spacing:2px;
  }
  .brand-mark__dot{width:22px;height:22px;border-radius:50%;background:var(--text-grey)}
  .back-url{
    position:absolute;left:0;right:0;top:341px;text-align:center;
    font-family:"Montserrat",sans-serif;font-weight:600;font-size:17px;color:var(--text-grey);
  }
  .dot-row{position:absolute;left:0;right:0;top:387px;display:flex;justify-content:center;gap:11px}
  .dot-row__dot{width:10px;height:10px;border-radius:50%}
  .dot-row__dot--cyan{background:var(--dot-cyan)}
  .dot-row__dot--navy{background:var(--dot-navy)}
  .dot-row__dot--magenta{background:var(--dot-magenta)}
  .dot-row__dot--orange{background:var(--dot-orange)}
  .dot-row__dot--green{background:var(--dot-green)}
</style>
</head>
<body>
<main class="stage">

  <section class="card card--front" aria-label="Card front">
    <svg class="front-art" viewBox="0 0 907 518" aria-hidden="false">
      <defs>
        <linearGradient id="portraitTone" x1="0" y1="0" x2="0" y2="1">
          <stop offset="0" stop-color="#cfcfcf"/>
          <stop offset="0.55" stop-color="#3a3a3a"/>
          <stop offset="1" stop-color="#00a3e0" stop-opacity="0"/>
        </linearGradient>
      </defs>
      <g transform="translate(180 20) rotate(22)">
        <rect x="-600" y="-60" width="700" height="90" rx="45" fill="var(--band-grey-light)"/>
      </g>
      <g transform="translate(260 205) rotate(22)">
        <rect x="-600" y="-150" width="750" height="300" rx="150" fill="var(--band-grey)"/>
      </g>
      <g transform="translate(234 342) rotate(22)">
        <rect x="-700" y="-160" width="860" height="320" rx="160" fill="var(--brand-blue)"/>
      </g>
      <rect role="img" aria-label="Portrait photo of Renny Osbert, arms crossed, in greyscale" x="76" y="64" width="298" height="380" rx="60" fill="url(#portraitTone)"/>
    </svg>

    <h1 class="name">Renny Osbert</h1>
    <ul class="contact-list">
      <li class="contact-item">
        <svg class="contact-icon" viewBox="0 0 24 24"><path d="M6.6 10.8a15.1 15.1 0 0 0 6.6 6.6l2.2-2.2a1 1 0 0 1 1-.25 11.4 11.4 0 0 0 3.6.57 1 1 0 0 1 1 1V20a1 1 0 0 1-1 1A17 17 0 0 1 3 4a1 1 0 0 1 1-1h3.5a1 1 0 0 1 1 1c0 1.25.2 2.45.57 3.57a1 1 0 0 1-.25 1z"/></svg>
        AUSTRALIA: +61 491 352 864
      </li>
      <li class="contact-item">SINGAPORE: +65 8342 6109</li>
      <li class="contact-item">
        <svg class="contact-icon" viewBox="0 0 24 24"><path d="M2 5h20v14H2z M2 5l10 7 10-7" fill="var(--text-grey)"/><path d="M3 6l9 6.3L21 6" fill="none" stroke="#fff" stroke-width="1.6"/></svg>
        RENNY@RENNYOSBERT.EXAMPLE
      </li>
      <li class="contact-item">
        <svg class="contact-icon" viewBox="0 0 24 24"><circle cx="12" cy="12" r="10"/><path d="M7 7c2 0 3 1 3 3s-2 2-2 4 1 3 1 4M15 5c-1 2 0 3 2 3s3 2 2 4" fill="none" stroke="#fff" stroke-width="1.6"/></svg>
        WWW.RENNYOSBERT.EXAMPLE
      </li>
    </ul>
  </section>

  <section class="card card--back" aria-label="Card back">
    <div class="brand-mark">
      <span class="brand-mark__dot"></span>
      <span class="brand-mark__name">Halfway Pioneer</span>
    </div>
    <p class="back-url">WWW.HALFWAYPIONEER.EXAMPLE</p>
    <div class="dot-row">
      <span class="dot-row__dot dot-row__dot--cyan"></span>
      <span class="dot-row__dot dot-row__dot--navy"></span>
      <span class="dot-row__dot dot-row__dot--magenta"></span>
      <span class="dot-row__dot dot-row__dot--orange"></span>
      <span class="dot-row__dot dot-row__dot--green"></span>
    </div>
  </section>

</main>
</body>
</html>
```